Healthcare technology company needs website design

We need a logo for a new company based in the U.S. We develop software to assist consumers identifying lowest cost healthcare coverage methods, including insurance, discount cards, and cash options. We would like to see designs that use multiple shades of green with the optional addition of other complimentary colors. The final design should communicate a unique blend of saving money while receiving the healthcare you need.
Need the following pages/sections: Homepage, Solutions, About Us, Contact
Competitors: www.velorimed.example; www.qzplo.example

Target Market(s)

Businesses

Industry/Entity Type

Healthcare

Coding

Coded - Design and coding required

Number of Pages Required

4 page

Colors
0054AA
0677BA
7BADD7
CADEEF
E8F1F8
00AB8E
00BBA5
67D7C9
C6EFE9
E9F9F6

Requirements
Must have
• Matching color theme with logo
Nice to have
• Animated background

```html
<!DOCTYPE html>
<html lang="en">
<head>
<meta charset="utf-8">
<title>Fernleaf Health</title>
<link href="https://fonts.googleapis.com/css2?family=Poppins:wght@300;400;500;600;700;800&display=swap" rel="stylesheet">
<style>
:root{
  --blue-900:#0054AA;
  --blue-700:#0677BA;
  --blue-400:#7BADD7;
  --blue-200:#CADEEF;
  --blue-100:#E8F1F8;
  --green-700:#00AB8E;
  --green-600:#00BBA5;
  --green-400:#67D7C9;
  --green-200:#C6EFE9;
  --green-100:#E9F9F6;
  --ink:#111;
  --text:#555;
  --white:#fff;
}
*{box-sizing:border-box;margin:0;padding:0}
html,body{width:1200px;height:2636px;overflow:hidden;background:#fff}
body{font-family:'Poppins',sans-serif;color:var(--ink)}
.page{position:relative;width:1200px;height:2636px;overflow:hidden}
.abs{position:absolute}

/* hero */
.hero{position:absolute;left:0;top:0;width:1200px;height:690px;background:linear-gradient(120deg,#0a4fa8 0%,var(--blue-900) 45%,#0a62c4 100%)}
.hero-photo{position:absolute;left:150px;top:215px;width:880px;height:475px;background:linear-gradient(180deg,rgba(120,150,200,.35),rgba(40,70,130,.7));border-radius:60px 60px 0 0}
.brand{position:absolute;left:148px;top:25px;display:flex;align-items:center;gap:10px;color:#fff}
.brand-dot{width:44px;height:44px;border-radius:50%;background:var(--green-600)}
.brand-name{font-weight:700;font-size:21px;line-height:1;white-space:nowrap}
.nav a{position:absolute;top:40px;color:#fff;font-size:7.5px;font-weight:600;letter-spacing:2px;text-decoration:none;white-space:nowrap}
.nav a.active{border-bottom:1px solid var(--green-400);padding-bottom:5px}
.contact-top{position:absolute;top:34px;display:flex;align-items:center;gap:7px;color:#fff;font-size:9.5px;white-space:nowrap}
.ring{width:27px;height:27px;border-radius:50%;border:2px solid #fff;display:flex;align-items:center;justify-content:center;flex:none}
.hero-lead{position:absolute;left:320px;top:150px;width:560px;text-align:center;color:#fff;font-size:12px;line-height:20px}
.hero-title{position:absolute;left:150px;top:180px;width:900px;text-align:center;color:#fff;font-weight:800;font-size:152px;letter-spacing:-2px;line-height:190px}
.slides{position:absolute;left:50px;top:235px;color:rgba(255,255,255,.6);font-size:10px}
.slides .cur{color:#fff;font-weight:600;font-size:14px}
.slides .bar{width:1px;height:55px;background:rgba(255,255,255,.6);margin:8px 0 8px 8px}
.slides p{margin-bottom:26px}
.hero-rail{position:absolute;left:1082px;top:225px;width:1px;height:395px;background:rgba(255,255,255,.35)}
.hero-rail::before{content:"";position:absolute;left:-3px;top:-3px;width:7px;height:7px;border-radius:50%;background:var(--blue-400)}
.social-tab{position:absolute;left:1173px;top:292px;width:40px;height:108px;border-radius:20px;background:var(--green-700);display:flex;flex-direction:column;align-items:center;justify-content:space-around;padding:10px 0}
.social-tab i{width:6px;height:6px;border-radius:50%;background:#fff;margin-right:12px}
.scroll{position:absolute;left:1061px;top:610px;width:42px;height:148px;border-radius:21px;background:var(--blue-700);color:#fff;font-size:8px;letter-spacing:3px;writing-mode:vertical-rl;transform:rotate(180deg);display:flex;align-items:center;justify-content:center}

/* about */
.about{position:absolute;left:0;top:690px;width:1200px;height:322px;background:var(--blue-100)}
.about-photo{position:absolute;left:149px;top:637px;width:347px;height:375px;border-radius:174px 174px 0 0/170px 170px 0 0;background:linear-gradient(160deg,#e9e4de,#cfc2b5 55%,#a89582)}
.eyebrow{font-size:15px;letter-spacing:6px;font-weight:400}
.h2{font-weight:700;font-size:40px;line-height:44px}
.body{font-size:10.5px;line-height:20.5px;color:var(--text)}
.btn{display:inline-flex;align-items:center;justify-content:center;width:124px;height:32px;border-radius:16px;background:var(--green-700);color:#fff;font-size:9px;letter-spacing:4px;font-weight:500}

/* solutions */
.sol-icon{position:absolute;width:78px;height:78px;border-radius:22px;background:var(--green-700);transform:rotate(-12deg);display:flex;align-items:center;justify-content:center;box-shadow:0 10px 20px rgba(0,171,142,.25)}
.sol-icon.blue{background:var(--blue-900);box-shadow:0 10px 20px rgba(0,84,170,.25)}
.sol-icon svg{transform:rotate(12deg)}
.sol-label{position:absolute;font-size:12px;text-align:center;font-weight:500;line-height:17px}

/* feature */
.feature{position:absolute;left:0;top:1409px;width:1200px;height:395px;background:linear-gradient(90deg,var(--blue-900),#0a5ec0)}
.feature-photo{position:absolute;left:642px;top:1409px;width:415px;height:448px;border-radius:0 0 208px 208px;background:radial-gradient(circle at 50% 48%,#3fd7f0 0%,#0d6f9a 22%,#072a44 55%,#050d18 100%)}

/* dashboard */
.card{position:absolute;background:#fff;border-radius:6px;box-shadow:0 12px 30px rgba(0,60,120,.1)}
.tiny{font-size:6px;letter-spacing:1.5px;color:#333;font-weight:500}
.legend{display:flex;justify-content:space-between;font-size:7px;color:#777;margin-bottom:11px}
.legend span i{display:inline-block;width:8px;height:4px;border-radius:2px;margin-right:4px;vertical-align:middle}
.step{position:absolute;left:655px;width:400px}
.step-num{position:absolute;left:0;top:6px;width:22px;height:22px;border-radius:50%;font-size:9px;display:flex;align-items:center;justify-content:center}
.step h4{margin-left:34px;font-size:13px;font-weight:500}
.step p{margin-left:34px;font-size:10px;line-height:15.5px;color:#444}

/* footer */
.footer{position:absolute;left:0;top:2368px;width:1200px;height:268px;background:var(--blue-900);color:#fff}
.f-item{position:absolute;top:48px;display:flex;align-items:center;gap:14px;font-size:10.5px;line-height:15px;white-space:nowrap}
.f-circle{width:62px;height:62px;border-radius:50%;background:rgba(123,173,215,.75);display:flex;align-items:center;justify-content:center}
.f-line{position:absolute;top:0;width:1px;height:140px;background:rgba(123,173,215,.6)}
.f-line::after{content:"";position:absolute;left:-3px;bottom:-3px;width:7px;height:7px;border-radius:50%;background:var(--blue-400)}
.f-social{position:absolute;left:536px;top:168px;display:flex;gap:8px}
.f-social i{width:26px;height:26px;border-radius:50%;background:var(--green-700);display:block}
.f-nav{position:absolute;left:248px;top:212px;display:flex;gap:51px;font-size:10px;letter-spacing:2.5px;font-weight:500}
.copy{position:absolute;left:0;top:237px;width:1200px;text-align:center;font-size:8.5px;letter-spacing:1.5px}
</style>
</head>
<body>
<div class="page">

<!-- HERO -->
<section class="hero">
  <div class="hero-photo" role="img" aria-label="Team of five healthcare professionals in suits and face masks standing with arms crossed"></div>
  <div class="brand"><span class="brand-dot"></span><span class="brand-name">Fernleaf Health</span></div>
  <nav class="nav">
    <a class="active" style="left:483px">HOME</a>
    <a style="left:549px">SOLUTIONS</a>
    <a style="left:644px">ABOUT US</a>
    <a style="left:731px">CONTACT</a>
  </nav>
  <div class="contact-top" style="left:816px">
    <span class="ring"><svg width="11" height="8" viewBox="0 0 11 8"><rect x=".5" y=".5" width="10" height="7" fill="none" stroke="#fff"/><path d="M.5.5l5 4 5-4" fill="none" stroke="#fff"/></svg></span>info@fernleaf.example
  </div>
  <div class="contact-top" style="left:966px">
    <span class="ring"><svg width="11" height="11" viewBox="0 0 12 12"><path d="M3 1l2 2.5-1.3 1.4a7 7 0 003.4 3.4L8.5 7 11 9l-1.5 2C5 11 1 7 1 2.5z" fill="#fff"/></svg></span>020 5550 1934
  </div>
  <p class="hero-lead">Lorem ipsum dolor sit amet, consectetur adipiscing elit. Sit dolor turpis sed sodales amet. Lorem pretium a, justo, a quis dignissim orci nibh convallis.</p>
  <h1 class="hero-title">FERNLEAF</h1>
  <div class="slides"><p class="cur" style="margin:0">01</p><div class="bar"></div><p>02</p><p>03</p><p>04</p><p>05</p></div>
  <div class="hero-rail"></div>
  <div class="social-tab"><i></i><i></i><i></i><i></i></div>
</section>

<!-- ABOUT -->
<section class="about"></section>
<div class="about-photo" role="img" aria-label="Smiling mother and father hugging their laughing little daughter"></div>
<div class="scroll">SCROLL DOWN</div>
<div class="abs" style="left:552px;top:746px">
  <p class="eyebrow">ABOUT</p>
  <h2 class="h2">Our Company</h2>
  <p class="body" style="width:500px;font-size:10.2px;margin-top:16px">Lorem ipsum dolor sit amet, consectetur adipiscing elit. Gravida viverra scelerisque quis in mattis sollicitudin. Tincidunt dignissim amet, elementum sem platea pellentesque odio. Vivamus vitae, donec posuere orci pretium odio malesuada. Suspendisse in egestas lectus nunc. Neque et lectus elementum, enim nunc elit dignissim pellentesque massa. Et euismod turpis sed in vitae. Nisl, arcu ultricies ipsum molestie est est quis ut.</p>
  <span class="btn" style="margin-top:16px">KNOW MORE</span>
</div>

<!-- SOLUTIONS -->
<div class="abs" style="left:0;top:1068px;width:1200px;text-align:center">
  <p class="eyebrow">OUR</p>
  <h2 class="h2">Solutions</h2>
</div>
<svg class="abs" style="left:220px;top:1170px" width="790" height="150" viewBox="0 0 790 150">
  <path d="M10 50 C40 70 80 75 115 70" fill="none" stroke="#ddd" stroke-width="1.5"/>
  <path d="M150 45 C190 25 230 18 265 18" fill="none" stroke="#888" stroke-width="2"/>
  <path d="M320 45 C360 70 380 90 410 110" fill="none" stroke="#333" stroke-width="2"/>
  <path d="M490 130 C540 125 570 100 595 80" fill="none" stroke="#555" stroke-width="2"/>
  <path d="M675 105 C690 140 740 140 780 118" fill="none" stroke="#ccc" stroke-width="1.5"/>
</svg>
<div class="sol-icon" style="left:295px;top:1198px"><svg width="40" height="40" viewBox="0 0 40 40" fill="none" stroke="#fff" stroke-width="1.8"><circle cx="20" cy="14" r="7"/><path d="M20 10v8M18 12h3M17 16h4"/><path d="M4 30h8l6 3h10l8-6-3-2-8 4h-7"/></svg></div>
<div class="sol-icon blue" style="left:460px;top:1160px"><svg width="42" height="42" viewBox="0 0 42 42" fill="none" stroke="#fff" stroke-width="1.8"><path d="M5 20a16 16 0 0132 0c-3-3-6-3-8 0-2-3-6-3-8 0-2-3-6-3-8 0-2-3-5-3-8 0z"/><path d="M21 20v14a3 3 0 01-6 0"/><circle cx="13" cy="25" r="4"/></svg></div>
<div class="sol-icon" style="left:627px;top:1250px"><svg width="42" height="40" viewBox="0 0 42 40" fill="none" stroke="#fff" stroke-width="1.8"><rect x="10" y="6" width="26" height="18" rx="2"/><circle cx="23" cy="15" r="4"/><path d="M4 22v12h12l8-6-3-2-6 3"/></svg></div>
<div class="sol-icon" style="left:818px;top:1205px"><svg width="42" height="40" viewBox="0 0 42 40" fill="none" stroke="#fff" stroke-width="1.8"><circle cx="26" cy="14" r="9"/><path d="M22 18l8-8"/><circle cx="23" cy="11" r="1.2"/><circle cx="29" cy="17" r="1.2"/><path d="M4 26h8l6 3h8l8-5-3-2-7 3h-6"/></svg></div>
<p class="sol-label" style="left:268px;top:1298px;width:118px">Lowest cost healthcare coverage methods</p>
<p class="sol-label" style="left:420px;top:1258px;width:140px">Including insurance</p>
<p class="sol-label" style="left:610px;top:1345px;width:120px">Cash options</p>
<p class="sol-label" style="left:792px;top:1303px;width:120px">Discount cards</p>

<!-- FEATURE -->
<section class="feature"></section>
<div class="feature-photo" role="img" aria-label="Finger pressing a glowing cloud button surrounded by digital technology icons"></div>
<div class="abs" style="left:149px;top:1450px;color:#fff">
  <p class="eyebrow" style="letter-spacing:7px">FEATURE SOLUTION</p>
  <h2 class="h2" style="margin-top:6px">Pre-Adjudication<br>Platform</h2>
  <p class="body" style="color:#fff;width:425px;margin-top:22px">Lorem ipsum dolor sit amet, consectetur adipiscing elit. Gravida viverra scelerisque quis in mattis sollicitudin. Tincidunt dignissim amet, elementum sem platea pellentesque odio. Vivamus vitae, donec posuere orci pretium odio malesuada. Suspendisse in egestas lectus nunc. Neque et lectus elementum, enim nunc elit dignissim pellentesque massa. Et euismod turpis sed in vitae. Nisl, arcu ultricies ipsum molestie est est quis ut.</p>
  <span class="btn" style="margin-top:24px">KNOW MORE</span>
</div>

<!-- DASHBOARD -->
<div class="abs" style="left:180px;top:1935px;width:300px;height:300px;border-radius:50%;background:var(--blue-100)"></div>
<div class="card" style="left:156px;top:1905px;width:175px;height:70px;padding:14px 16px">
  <p class="tiny">APPLICATIONS</p><p style="font-size:18px;margin-top:6px">12.2k</p>
  <svg class="abs" style="right:12px;top:9px" width="54" height="54"><circle cx="27" cy="27" r="24" fill="none" stroke="#fde1e1" stroke-width="3"/><circle cx="27" cy="27" r="24" fill="none" stroke="#f06363" stroke-width="3" stroke-dasharray="120 151" transform="rotate(-90 27 27)"/><text x="27" y="31" font-size="11" fill="#f06363" text-anchor="middle" font-family="Poppins">+20%</text></svg>
</div>
<div class="card" style="left:146px;top:1998px;width:202px;height:140px;padding:14px 4px">
  <p style="font-size:11px;font-weight:600">68%</p><p style="font-size:6px;color:#888">Lorem ipsum is simply</p>
  <p class="abs" style="right:10px;top:18px;font-size:5px;color:#f06363">● Point me</p>
  <p class="abs" style="left:80px;top:66px;font-size:5.5px;color:#888">Many variations $2,435</p>
  <svg class="abs" style="left:0;top:50px" width="202" height="70"><path d="M2 60 C20 30 30 45 50 55 S90 30 115 30 S150 50 165 35 S190 12 200 8" fill="none" stroke="#f4a52a" stroke-width="2"/><circle cx="115" cy="30" r="3" fill="#fff" stroke="#f06363" stroke-width="1.5"/></svg>
  <div class="abs" style="left:12px;top:126px;width:180px;display:flex;justify-content:space-between;font-size:5.5px;color:#888"><span>Sep</span><span>Oct</span><span>Nov</span><span>Dec</span><span>Jan</span><span>Feb</span></div>
</div>
<div class="abs" style="left:365px;top:1935px;width:125px;height:125px;border-radius:8px;background:linear-gradient(160deg,var(--green-400),var(--green-700));color:#fff;padding:14px 12px;box-shadow:0 14px 30px rgba(0,171,142,.3)">
  <p style="font-size:8px">Savings</p><p style="font-size:16px;font-weight:600;margin-top:42px">23.57%</p><p style="font-size:7px">Accusamus et iusto</p>
</div>
<div class="card" style="left:410px;top:2080px;width:175px;height:70px;padding:18px 8px">
  <p class="tiny">DISCOUNT CARDS</p><p style="font-size:16px;margin-top:6px">11.1k</p>
  <svg class="abs" style="right:12px;top:8px" width="56" height="56"><circle cx="28" cy="28" r="25" fill="none" stroke="var(--green-200)" stroke-width="3"/><circle cx="28" cy="28" r="25" fill="none" stroke="var(--green-600)" stroke-width="3" stroke-dasharray="120 157" transform="rotate(-90 28 28)"/><text x="28" y="32" font-size="11" fill="var(--green-600)" text-anchor="middle" font-family="Poppins">+20%</text></svg>
</div>
<div class="abs" style="left:204px;top:2172px;width:116px;height:115px;border-radius:8px;background:linear-gradient(160deg,#2b6fd6,#1b4fc8);color:#fff;padding:12px;box-shadow:0 14px 30px rgba(0,84,170,.3)">
  <p style="font-size:8px">Reach</p><p style="font-size:16px;font-weight:600;margin-top:28px">18 <span style="font-size:8px;font-weight:400;opacity:.8">▲ 12%</span></p><p style="font-size:8px">New Candidated</p>
</div>
<div class="card" style="left:349px;top:2172px;width:142px;height:138px;padding:12px 10px">
  <div style="display:flex;justify-content:space-between;font-size:8px;margin-bottom:24px"><span>Acquisitions</span><span style="color:#2b6fd6;font-size:6px">This Month</span></div>
  <div class="legend"><span><i style="background:#a45ee5"></i>Application</span><b>64%</b></div>
  <div class="legend"><span><i style="background:#1ec6e6"></i>Shortlisted</span><b>18%</b></div>
  <div class="legend"><span><i style="background:#f4a52a"></i>On-Hold</span><b>10%</b></div>
  <div class="legend"><span><i style="background:#f06363"></i>Rejected</span><b>8%</b></div>
</div>

<!-- PRESCRIPTION -->
<h2 class="h2 abs" style="left:655px;top:1912px;width:400px">Prescription Drug Landscape</h2>
<div class="step" style="top:2023px"><span class="step-num" style="background:var(--green-700);color:#fff">01</span><h4 style="color:var(--green-700)">Lorem ipsum dolor sit amet,</h4><p>On the other hand, we denounce with righteous indignation and dislike men who are so beguiled and demoralized by the charms of pleasure of the moment,</p></div>
<div class="step" style="top:2110px"><span class="step-num" style="border:1px solid #8aa;color:#678">02</span><h4>Consectetur adipiscing elit.</h4><p>On the other hand, we denounce with righteous indignation and dislike men who are so beguiled and demoralized by the charms of pleasure of the moment, so blinded</p></div>
<div class="step" style="top:2205px"><span class="step-num" style="border:1px solid #8aa;color:#678">03</span><h4>Voluptatem sequi nesciunt</h4><p>On the other hand, we denounce with righteous indignation and dislike men who are so beguiled and demoralized by the charms of pleasure of the moment,</p></div>

<!-- FOOTER -->
<footer class="footer">
  <span class="f-line" style="left:360px"></span><span class="f-line" style="left:600px"></span><span class="f-line" style="left:841px"></span>
  <div class="f-item" style="left:142px"><span class="f-circle"><svg width="14" height="18" viewBox="0 0 14 18"><path d="M7 0a7 7 0 017 7c0 5-7 11-7 11S0 12 0 7a7 7 0 017-7z" fill="#fff"/><circle cx="7" cy="7" r="2.5" fill="#7BADD7"/></svg></span><span>4410 Linden Ave.<br>Westbrook, RI 02800</span></div>
  <div class="f-item" style="left:405px"><span class="f-circle"><svg width="14" height="14" viewBox="0 0 12 12"><path d="M3 1l2 2.5-1.3 1.4a7 7 0 003.4 3.4L8.5 7 11 9l-1.5 2C5 11 1 7 1 2.5z" fill="#fff"/></svg></span><span>020 5550 1934</span></div>
  <div class="f-item" style="left:653px"><span class="f-circle"><svg width="14" height="14" viewBox="0 0 14 14"><rect x="1" y="2" width="12" height="11" rx="1" fill="#fff"/><rect x="1" y="2" width="12" height="3" fill="#dbe8f5"/></svg></span><span>Monday-Friday</span></div>
  <div class="f-item" style="left:871px"><span class="f-circle"><svg width="14" height="10" viewBox="0 0 11 8"><rect width="11" height="8" fill="#fff"/><path d="M0 0l5.5 4L11 0" fill="none" stroke="#7BADD7"/></svg></span><span>info@fernleaf.example</span></div>
  <div class="f-social"><i></i><i></i><i></i><i></i></div>
  <nav class="f-nav"><span>HOME</span><span>SOLUTIONS</span><span>ABOUT US</span><span>CONTACT</span><span>PRIVACY POLICY</span><span>TERMS OF USE</span></nav>
  <p class="copy">Copyright ©2022 Fernleaf Health. All Rights Reserved.</p>
</footer>

</div>
</body>
</html>
```